Marevanga Wines

A Red Wine Label for future Wine Concept called Marevanga Wine. The back label will have the following words which capture the essence of the wine "I am sworn to the secrecy about the origins of this wine but I can assure you it’s from the best cellars of Africa. Marevanga is an African (Shona) name which loosely means honour, praise or to be held in high exteem. Hold on to your hats because this wine is a whirlwind of flavours. It's dark, spicy and fruity flavours will attack the palate with warm aggression and intent whilst being served with Sadza/ Nsima and roasted beef accompanied with mufushwa (dried vegetables) cooked in grounded nut paste. The inspiring flame, style and mood of an African braai, together with its outlandish flavours popping in and out of the glass, Marevanga will make every serving a gesture of respect and distinction!!!"
Updates

I will be buying wine packed in unbranded bottles then Brand it as Marevanga on my own Marevanga label for some African event theme. The wines will be South African a Shiraz. So I need a back label with message placed in brief and front label for a red wine bottle. I have attached some old labels for the wine so I need a redesign of the l label for have a morden and African feel to it                                   

Please

Target Market(s)

Appeal to general populace and those with an afrocentric feel

Requirements
Must have
• Back and front labels, simplicity
Should not have
• Too many colours

```html
<!DOCTYPE html>
<html lang="en">
<head>
<meta charset="utf-8">
<title>Marevanga Shiraz — Front and Back Labels</title>
<link rel="stylesheet" href="https://fonts.googleapis.com/css2?family=Josefin+Sans:wght@200;300&family=Open+Sans:wght@400&display=swap">
<style>
  :root {
    --backdrop-top: #120606;
    --backdrop-bottom: #4e1812;
    --label-cream: #fff4cf;
    --ink: #111111;
    --frame-line: #3a3a3a;
    --cluster-light: #e9c766;
    --cluster-deep: #b9733a;
    --leaf-light: #e8b35c;
    --leaf-deep: #a86d32;
  }
  * { box-sizing: border-box; margin: 0; padding: 0; }
  html, body { width: 1200px; height: 754px; overflow: hidden; }
  body {
    position: relative;
    background: linear-gradient(180deg, var(--backdrop-top) 0%, var(--backdrop-bottom) 100%);
    color: var(--ink);
  }
  .label {
    position: absolute;
    top: 22px;
    width: 446px;
    height: 712px;
    background: var(--label-cream);
  }
  .label--front { left: 60px; }
  .label--back { left: 704px; }
  .label__frame {
    position: absolute;
    inset: 11px;
    border: 1px solid var(--frame-line);
  }
  .grape-cluster {
    position: absolute;
    left: 150px;
    top: 158px;
    width: 150px;
    height: 234px;
    border-radius: 6px;
    background: linear-gradient(180deg, var(--cluster-light), var(--cluster-deep));
  }
  .wine-name {
    position: absolute;
    left: 0; right: 0;
    top: 458px;
    text-align: center;
    font-family: "Josefin Sans", sans-serif;
    font-weight: 200;
    font-size: 45px;
    letter-spacing: 1px;
    line-height: 1;
  }
  .varietal {
    position: absolute;
    left: 0; right: 0;
    top: 516px;
    text-align: center;
    font-family: "Josefin Sans", sans-serif;
    font-weight: 300;
    font-size: 21px;
    letter-spacing: 1px;
  }
  .origin {
    position: absolute;
    left: 0; right: 0;
    top: 619px;
    text-align: center;
    font-family: "Open Sans", sans-serif;
    font-size: 19px;
    line-height: 26px;
  }
  .vine-leaves {
    position: absolute;
    left: 118px;
    top: 42px;
    width: 178px;
    height: 226px;
    border-radius: 6px;
    background: linear-gradient(180deg, var(--leaf-light), var(--leaf-deep));
  }
  .story {
    position: absolute;
    left: 52px;
    width: 342px;
    top: 300px;
    text-align: center;
    font-family: "Open Sans", sans-serif;
    font-size: 12.8px;
    line-height: 17.6px;
  }
  .award-mark {
    position: absolute;
    left: 206px;
    top: 616px;
    width: 30px;
    height: 58px;
  }
</style>
</head>
<body>
  <section class="label label--front">
    <div class="label__frame"></div>
    <div class="grape-cluster" role="img" aria-label="Grape cluster illustration made of striped circles in green, yellow, red and black"></div>
    <h1 class="wine-name">MAREVANGA</h1>
    <p class="varietal">SHIRAZ</p>
    <p class="origin">South Africa<br>2005</p>
  </section>

  <section class="label label--back">
    <div class="label__frame"></div>
    <div class="vine-leaves" role="img" aria-label="Vine leaves with curling tendrils, filled with African geometric pattern in ochre and brown"></div>
    <p class="story">
      I am sworn to the secrecy about the origins<br>
      of this wine but I can assure you it’s from the<br>
      best cellars of Africa. Marevanga is an African<br>
      (Shona) name which loosely means honour,<br>
      praise or to be held in high exteem. Hold on<br>
      to your hats because this wine is a whirlwind<br>
      of flavours. It's dark, spicy and fruity flavours<br>
      will attack the palate with warm aggression<br>
      and intent whilst being served with Sadza/<br>
      Nsima and roasted beef accompanied with<br>
      mufushwa (dried vegetables) cooked in<br>
      grounded nut paste. The inspiring flame,<br>
      style and mood of an African braai, together<br>
      with its outlandish flavours popping in and<br>
      out of the glass, Marevanga will make every<br>
      serving a gesture of respect and distinction!
    </p>
    <svg class="award-mark" viewBox="0 0 30 58" aria-hidden="true">
      <path fill="var(--ink)" d="M9 24 L4 56 L11 50 L15 57 L16 28 Z M21 24 L26 56 L19 50 L15 57 L14 28 Z"/>
      <circle cx="15" cy="15" r="14" fill="var(--ink)"/>
    </svg>
  </section>
</body>
</html>
```